Brissett Plumbing van wrap

Van wrap with logo and list of services
Water Heaters
Sump Pumps
Drain Cleaning
Waterlines
Drain Lines
Boilers
Garbage Disposals
Tub/Showers
Gas Lines
Bathroom Remodels
and More!

Phone: 585-555-0143
brissettplumbing-example.com

slogan:
Dog Owned and Family Operated

Instagram ID : BrissettPlumbingLLC
Facebook ID : BrissettPlumbingLLC

I need to adjust these for a 2013 Varnell cargoline as well if possible

```html
<!DOCTYPE html>
<html lang="en">
<head>
<meta charset="utf-8">
<title>Brissett Plumbing – Van Wrap</title>
<link rel="stylesheet" href="https://fonts.googleapis.com/css2?family=Oswald:wght@500;700&family=Poppins:wght@600;700&display=swap">
<style>
  :root {
    --wrap-red: #d3262f;
    --wrap-red-dark: #a81b24;
    --wrap-navy: #101a33;
    --wrap-tan: #d8c3a0;
    --wrap-teal: #1f8fb8;
    --glass: #2b303b;
    --trim: #2a2b2f;
    --ink-light: #ffffff;
    --canvas: #ffffff;
  }
  html, body {
    margin: 0;
    padding: 0;
    width: 1200px;
    height: 1200px;
    overflow: hidden;
    background: var(--canvas);
  }
  .wrap-sheet { display: block; width: 1200px; height: 1200px; }
  .fill-red { fill: var(--wrap-red); }
  .fill-navy { fill: var(--wrap-navy); }
  .fill-tan { fill: var(--wrap-tan); }
  .fill-teal { fill: var(--wrap-teal); }
  .fill-glass { fill: var(--glass); }
  .fill-trim { fill: var(--trim); }
  .mascot-area { fill: url(#mascotTone); }
  .brand-name {
    font-family: "Oswald", sans-serif;
    font-weight: 700;
    fill: var(--ink-light);
    text-anchor: middle;
    letter-spacing: 1px;
  }
  .service-item {
    font-family: "Oswald", sans-serif;
    font-weight: 700;
    font-size: 10.5px;
    fill: var(--ink-light);
  }
  .service-dot { fill: var(--wrap-teal); }
  .slogan {
    font-family: "Oswald", sans-serif;
    font-weight: 500;
    fill: var(--wrap-tan);
    letter-spacing: 3px;
  }
  .phone {
    font-family: "Poppins", sans-serif;
    font-weight: 700;
    fill: var(--ink-light);
  }
  .web {
    font-family: "Poppins", sans-serif;
    font-weight: 600;
    fill: var(--ink-light);
  }
  .social-handle {
    font-family: "Poppins", sans-serif;
    font-weight: 600;
    font-size: 6px;
    fill: var(--ink-light);
  }
  .rear-services {
    font-family: "Oswald", sans-serif;
    font-weight: 500;
    font-size: 7.6px;
    fill: var(--ink-light);
    text-anchor: middle;
  }
</style>
</head>
<body>
<svg class="wrap-sheet" viewBox="0 0 974 974" xmlns="http://www.w3.org/2000/svg">
  <defs>
    <radialGradient id="mascotTone" cx="50%" cy="45%" r="60%">
      <stop offset="0%" stop-color="#d9402f"/>
      <stop offset="70%" stop-color="#b52a25"/>
      <stop offset="100%" stop-color="#2a8fc0"/>
    </radialGradient>
    <clipPath id="sidePanelClip">
      <path d="M70 378 L72 318 Q80 262 150 236 L236 168 Q262 128 330 120 L858 114 Q896 116 898 150 L902 380 Z"/>
    </clipPath>
    <clipPath id="rearPanelClip">
      <path d="M62 790 L64 590 Q66 560 100 556 L250 556 Q284 560 286 590 L288 790 Z"/>
    </clipPath>
  </defs>

  <!-- Side wrap panel -->
  <g class="side-panel" clip-path="url(#sidePanelClip)">
    <rect class="fill-red" x="60" y="100" width="850" height="300"/>
    <polygon class="fill-navy" points="300,100 910,100 910,118 560,150 330,200 300,200"/>
    <polygon class="fill-tan" points="330,200 560,150 910,118 910,124 560,157 340,208"/>
    <polygon class="fill-navy" points="600,100 910,100 910,112 700,140"/>
    <polygon class="fill-tan" points="360,345 880,258 910,256 910,262 880,265 362,352"/>
    <polygon class="fill-navy" points="362,352 910,262 910,400 270,400 270,368"/>
    <polygon class="fill-teal" points="275,400 880,352 910,350 910,366 880,368 275,412"/>
    <path class="fill-glass" d="M206 262 L248 186 Q262 162 300 160 L372 158 L372 268 Z"/>
    <rect class="fill-trim" x="60" y="378" width="850" height="22"/>
  </g>

  <rect class="mascot-area" x="455" y="130" width="105" height="110" rx="52" role="img" aria-label="Illustrated red dog mascot wearing a cap, holding a wrench"/>
  <text class="brand-name" x="515" y="278" font-size="40">BRISSETT</text>
  <text class="brand-name" x="515" y="300" font-size="17" letter-spacing="4">PLUMBING</text>

  <g class="services-side">
    <g transform="translate(672 184)">
      <circle class="service-dot" cx="-4" cy="-3.5" r="1.8"/><text class="service-item" x="0" y="0">WATER HEATERS</text>
      <circle class="service-dot" cx="-4" cy="8.5" r="1.8"/><text class="service-item" x="0" y="12">DRAIN CLEANING</text>
      <circle class="service-dot" cx="-4" cy="20.5" r="1.8"/><text class="service-item" x="0" y="24">DRAIN LINES</text>
      <circle class="service-dot" cx="-4" cy="32.5" r="1.8"/><text class="service-item" x="0" y="36">GARBAGE DISPOSALS</text>
      <circle class="service-dot" cx="-4" cy="44.5" r="1.8"/><text class="service-item" x="0" y="48">GAS LINES</text>
      <circle class="service-dot" cx="-4" cy="56.5" r="1.8"/><text class="service-item" x="0" y="60">AND MORE!</text>
    </g>
    <g transform="translate(772 175)">
      <circle class="service-dot" cx="-4" cy="-3.5" r="1.8"/><text class="service-item" x="0" y="0">SUMP PUMPS</text>
      <circle class="service-dot" cx="-4" cy="8.5" r="1.8"/><text class="service-item" x="0" y="12">WATERLINES</text>
      <circle class="service-dot" cx="-4" cy="20.5" r="1.8"/><text class="service-item" x="0" y="24">BOILERS</text>
      <circle class="service-dot" cx="-4" cy="32.5" r="1.8"/><text class="service-item" x="0" y="36">TUB/SHOWERS</text>
      <circle class="service-dot" cx="-4" cy="44.5" r="1.8"/><text class="service-item" x="0" y="48">BATHROOM REMODELS</text>
    </g>
  </g>

  <text class="phone" x="210" y="303" font-size="16">585-555-0143</text>
  <text class="web" x="211" y="320" font-size="11">brissettplumbing-example.com</text>

  <text class="slogan" x="486" y="352" font-size="15" transform="rotate(-9 486 352)">DOG OWNED AND FAMILY OPERATED</text>

  <circle cx="778" cy="327" r="5" class="fill-teal"/>
  <text class="social-handle" x="787" y="329">@BrissettPlumbingLLC</text>

  <!-- Rear wrap panel -->
  <g class="rear-panel" clip-path="url(#rearPanelClip)">
    <rect class="fill-red" x="60" y="550" width="230" height="245"/>
    <rect class="fill-navy" x="60" y="664" width="230" height="126"/>
    <rect class="fill-teal" x="68" y="686" width="100" height="16"/>
    <rect class="fill-tan" x="60" y="662" width="230" height="2"/>
  </g>
  <rect class="mascot-area" x="145" y="566" width="62" height="58" rx="29" role="img" aria-label="Illustrated red dog mascot wearing a cap"/>
  <text class="brand-name" x="175" y="648" font-size="26">BRISSETT</text>
  <text class="brand-name" x="175" y="660" font-size="9" letter-spacing="3">PLUMBING</text>
  <text class="slogan" x="175" y="680" font-size="8.5" letter-spacing="1.5" text-anchor="middle">DOG OWNED AND FAMILY OPERATED</text>
  <text class="phone" x="118" y="699" font-size="11" text-anchor="middle">585-555-0143</text>
  <text class="web" x="226" y="698" font-size="7" text-anchor="middle">brissettplumbing-example.com</text>
  <text class="rear-services" x="175" y="718">WATER HEATERS • SUMP PUMPS • DRAIN CLEANING • WATERLINES</text>
  <text class="rear-services" x="175" y="730">DRAIN LINES • BOILERS • GARBAGE DISPOSALS • TUB/SHOWERS</text>
  <text class="rear-services" x="175" y="742">GAS LINES • BATHROOM REMODELS • AND MORE!</text>

  <!-- Front wrap panels -->
  <g class="front-panel">
    <path class="fill-navy" d="M358 600 L362 575 Q366 562 390 560 L565 560 Q590 562 594 575 L598 600 Z"/>
    <rect class="fill-glass" x="368" y="600" width="220" height="80" rx="6"/>
    <path class="fill-red" d="M352 680 L604 680 L606 760 L350 760 Z"/>
    <polygon class="fill-tan" points="358,600 368,600 368,640 360,640"/>
    <polygon class="fill-tan" points="588,600 598,600 596,640 588,640"/>
    <text class="phone" x="478" y="589" font-size="15" text-anchor="middle">585-555-0143</text>
    <text class="brand-name" x="478" y="712" font-size="16">BRISSETT PLUMBING</text>
  </g>
  <g class="front-panel" transform="translate(310 0)">
    <path class="fill-navy" d="M358 600 L362 575 Q366 562 390 560 L565 560 Q590 562 594 575 L598 600 Z"/>
    <rect class="fill-glass" x="368" y="600" width="220" height="80" rx="6"/>
    <path class="fill-red" d="M352 680 L604 680 L606 760 L350 760 Z"/>
    <polygon class="fill-tan" points="358,600 368,600 368,640 360,640"/>
    <polygon class="fill-tan" points="588,600 598,600 596,640 588,640"/>
    <text class="phone" x="478" y="589" font-size="15" text-anchor="middle">585-555-0143</text>
    <text class="brand-name" x="478" y="712" font-size="16">BRISSETT PLUMBING</text>
  </g>
</svg>
</body>
</html>
```